PathVerdanta: Course with Coaching for Next Generation Leaders - needs brochure designer!

We need a brief, beautiful brochure to share a new solution for students and career transitioners struggling with the changing economy of "jobs"....Our enterprise is trademarked as PathVerdanta (which is derived from the notion of Careers in a changing "Ecosystem" globally as well as locally....)We are developing an online collaboration course platform to support students, career transitioners and changemakers! There are 4 phases in a process that extends over 1 year, with interactive coaching and mentoring throughout the process. We emphasize the combined offering of "course, coaching, community"... The community component will feature collaborative exchange around large global issues with focus in sustainable development goals i.e. food, water, energy, health, technology, entrepreneurship... Success stories of next generation leaders in action will be featured via the continuous blog and also support microblog/ facebook/ social media community building and marketing channels. So the design needed will pitch multiple values from individual to community benefits, local to global...economic, environment & "equity" or education or social...you get the idea! We have a website started that you can view....http://www.pathverdanta.example

Target Market(s)

High School, College, University, Graduate, Early Career/ Career Transitioners with focus on "sustainability" issues - interested in developing expanded collaboration across discipline areas to foster more opportunities for learning, experiential projects, jobs, mentors, etc.

Industry/Entity Type

Education

Font styles to use
Sans Serif

Colors
0355a3
00a990
abd037
0792cd

Requirements
Must have
• 4 phases represented to outline process:
• Clarify, Communicate, Collaborate, Create!
• maybe a new infographic?
• must illustrate that the process moves from "all alone" individualism to coaching partner, to "Board of Advisors" and team projects...to empowered creativity with partners - locally and globally.
• Must show collaboration involves existing leaders & next generation working together - in the field, but also in professional contexts (that look like they are not just volunteers ha ha)
• Some way to show "on the ground experience" combined with "global perspective" and maybe globally reaching impact or relationships?
• It's a course...there is homework....but it is for the person and there are no grades :-)
• There is a "new path" necessary for everybody to keep learning -- udpating career relevance --
• "leadership" is a whole new paradigm of human ingenuity across sectors and often grassroots community centered enterprise... rather than top down....
Nice to have
• Show that communications and collaboration happens both online & in person -
• and may involve private one to one coaching and also group exchanges.
• Show how working in a community provides creative support, resources, opportunities to find the "hidden job market" through community networks where "projects" become "accomplishments" with "references".
• Entrepreneurship for Careers --is for everyone at every age and you don't have to be "in school"....
Should not have
• boring references just to resumes- or look like an online course that you have to do alone without any recognition or relationship building.

```html
<!DOCTYPE html>
<html lang="en">
<head>
<meta charset="utf-8">
<title>PathVerdanta Brochure</title>
<link href="https://fonts.googleapis.com/css2?family=Montserrat:wght@400;500;600;700&display=swap" rel="stylesheet">
<style>
  :root{
    --stage:#262626;
    --paper:#ffffff;
    --sky:#39a8e0;
    --lime:#8dc63f;
    --teal:#006f6d;
    --teal-text:#0e7470;
    --blue-circle:#1a8fd6;
    --green-circle:#6aa83c;
    --ink:#222222;
    --ink-soft:#333333;
    --phone-blue:#2c5aa8;
  }
  *{margin:0;padding:0;box-sizing:border-box}
  html,body{width:1200px;height:1200px;overflow:hidden;background:var(--stage)}
  body{font-family:"Montserrat",sans-serif;position:relative}
  .brochure{
    position:absolute;left:220px;top:62px;width:953px;height:1343px;
    background:var(--paper);transform:scale(0.8);transform-origin:0 0;overflow:hidden;
  }
  .brand{position:absolute;left:563px;top:30px;display:flex;align-items:center;gap:12px}
  .brand-dot{width:86px;height:86px;border-radius:50%;background:var(--teal)}
  .brand-name{font-size:28px;font-weight:700;color:var(--ink)}
  .hero-photo{
    position:absolute;left:0;top:139px;width:502px;height:678px;
    background:linear-gradient(180deg,#1e8fd3 0%,#2b9ad9 45%,#2f8f9a 60%,#1e8fd3 100%);
  }
  .headline{
    position:absolute;left:23px;top:524px;width:452px;height:170px;background:var(--paper);
    padding:22px 0 0 18px;font-size:35px;font-weight:700;line-height:41px;color:var(--ink);white-space:nowrap;
  }
  .headline .accent{color:var(--blue-circle)}
  .phase{position:absolute;left:502px;width:451px;padding:20px 0 0 18px;color:#fff}
  .phase h2{display:flex;align-items:center;gap:8px;font-size:25px;font-weight:500;letter-spacing:.5px;
    width:340px;padding-bottom:8px;border-bottom:1px solid rgba(255,255,255,.7);margin-bottom:8px}
  .phase p{font-size:16.5px;font-weight:500;line-height:22px;letter-spacing:.3px;white-space:nowrap}
  .phase-clarify{top:139px;height:170px;background:var(--sky)}
  .phase-communicate{top:309px;height:170px;background:var(--lime)}
  .phase-collaborate{top:479px;height:168px;background:var(--teal)}
  .phase-create{top:647px;height:170px;background:var(--sky)}
  .tagline{position:absolute;top:855px;left:0;width:953px;text-align:center;
    font-size:28px;font-weight:700;color:var(--teal-text)}
  .tag-rule{position:absolute;top:900px;left:90px;width:785px;height:1px;background:var(--teal)}
  .subline{position:absolute;top:912px;left:0;width:965px;text-align:center;font-size:18.5px;color:var(--ink-soft)}
  .steps{position:absolute;top:962px;left:0;width:953px;height:220px}
  .step{position:absolute;width:160px;text-align:center}
  .step-circle{width:154px;height:154px;border-radius:50%;margin:0 auto;display:flex;align-items:center;justify-content:center}
  .step-label{margin-top:14px;margin-left:-40px;margin-right:-40px;font-size:23px;font-weight:700;line-height:29px;color:var(--ink-soft);white-space:nowrap}
  .chev{position:absolute;top:50px}
  .region-rule{position:absolute;top:1219px;left:90px;width:785px;height:4px;border-top:1px solid var(--teal);border-bottom:1px solid var(--teal)}
  .region{position:absolute;top:1207px;left:251px;width:451px;height:41px;background:var(--ink);color:#fff;
    font-size:19px;text-align:center;line-height:41px;letter-spacing:.3px}
  .contact{position:absolute;top:1272px;left:84px;display:flex;align-items:center;gap:10px;
    font-size:24px;font-weight:700;color:var(--ink-soft);white-space:nowrap}
  .contact .web{margin-left:26px}
</style>
</head>
<body>
<main class="brochure">
  <div class="brand"><span class="brand-dot"></span><span class="brand-name">PathVerdanta</span></div>

  <div class="hero-photo" role="img" aria-label="Photo of three smiling students holding notebooks and a laptop"></div>

  <div class="headline">Empowered Creativity<br>with Partners -<br><span class="accent">Locally and Globally.</span></div>

  <section class="phase phase-clarify">
    <h2><svg width="30" height="26" viewBox="0 0 30 26" fill="none" stroke="#fff" stroke-width="2.5"><circle cx="15" cy="11" r="7"/><line x1="20" y1="16" x2="27" y2="23"/><line x1="2" y1="13" x2="7" y2="13"/></svg>CLARIFY</h2>
    <p>Personal Profile &amp; Mission<br>Field Functional Niche Organizational Targets<br>SWOT: Strenghts, Weakness, Opportunity</p>
  </section>
  <section class="phase phase-communicate">
    <h2><svg width="30" height="26" viewBox="0 0 30 26" fill="none" stroke="#fff" stroke-width="2.5"><path d="M2 8l8-4 5 4 5-4 8 4-6 8-7 5-7-5z"/></svg>COMMUNICATE</h2>
    <p>Professional Presentation (Resumes,<br>Cover, ProNetly)<br>Learning &amp; professional Development<br>Marketing YOU?Professional Branding</p>
  </section>
  <section class="phase phase-collaborate">
    <h2><svg width="30" height="28" viewBox="0 0 30 28" fill="#fff"><circle cx="15" cy="6" r="4"/><path d="M8 20c0-6 3-9 7-9s7 3 7 9z"/><circle cx="3" cy="20" r="2.5"/><circle cx="27" cy="20" r="2.5"/><circle cx="15" cy="25" r="2.5"/></svg>COLLABORATE</h2>
    <p>Profeesional Networking<br>Build Board of Advisors<br>Niche Project &amp; Partners<br>SMART Performace</p>
  </section>
  <section class="phase phase-create">
    <h2><svg width="30" height="26" viewBox="0 0 30 26" fill="none" stroke="#fff" stroke-width="2.5"><circle cx="17" cy="13" r="6"/><line x1="2" y1="10" x2="8" y2="10"/><line x1="2" y1="16" x2="8" y2="16"/><line x1="17" y1="2" x2="17" y2="5"/><line x1="26" y1="13" x2="29" y2="13"/></svg>CREATE!!</h2>
    <p>Presentations, Forums, Conferences<br>Gap Analysis Research Stakeolders &amp; Solutions<br>Job Search Strategy: Negotiate Win/Wins!<br>Entrepreneurship for Evolving Careers</p>
  </section>

  <h3 class="tagline">Private one to one coaching and also group exchanges</h3>
  <div class="tag-rule"></div>
  <p class="subline">It's a course...there is homework....but it is for the person and there are no grades</p>

  <div class="steps">
    <div class="step" style="left:49px">
      <div class="step-circle" style="background:var(--blue-circle)">
        <svg width="40" height="100" viewBox="0 0 40 100" fill="#fff"><circle cx="20" cy="9" r="8"/><rect x="6" y="20" width="28" height="38" rx="5"/><rect x="10" y="56" width="8" height="42"/><rect x="22" y="56" width="8" height="42"/></svg>
      </div>
      <div class="step-label">Individual</div>
    </div>
    <svg class="chev" style="left:212px" width="62" height="60" viewBox="0 0 64 60" fill="#222"><path d="M0 0h18l20 30-20 30H0l20-30z"/><path d="M26 0h18l20 30-20 30H26l20-30z"/></svg>
    <div class="step" style="left:280px">
      <div class="step-circle" style="background:var(--green-circle)">
        <svg width="90" height="90" viewBox="0 0 90 90" fill="none" stroke="#fff" stroke-width="4"><rect x="20" y="6" width="50" height="24"/><path d="M12 48h66l-10 28H22z" fill="#fff"/><circle cx="14" cy="52" r="6" fill="#fff"/><circle cx="76" cy="52" r="6" fill="#fff"/></svg>
      </div>
      <div class="step-label">Coaching<br>Partner</div>
    </div>
    <svg class="chev" style="left:448px" width="62" height="60" viewBox="0 0 64 60" fill="#222"><path d="M0 0h18l20 30-20 30H0l20-30z"/><path d="M26 0h18l20 30-20 30H26l20-30z"/></svg>
    <div class="step" style="left:518px">
      <div class="step-circle" style="background:var(--teal)">
        <svg width="90" height="90" viewBox="0 0 90 90" fill="#fff"><circle cx="25" cy="20" r="8"/><circle cx="45" cy="16" r="9"/><circle cx="65" cy="20" r="8"/><rect x="15" y="30" width="20" height="40" rx="5"/><rect x="34" y="28" width="22" height="46" rx="5"/><rect x="55" y="30" width="20" height="40" rx="5"/><ellipse cx="45" cy="80" rx="38" ry="6" fill="none" stroke="#fff" stroke-width="3"/></svg>
      </div>
      <div class="step-label">Board of<br>Advisors</div>
    </div>
    <svg class="chev" style="left:685px" width="62" height="60" viewBox="0 0 64 60" fill="#222"><path d="M0 0h18l20 30-20 30H0l20-30z"/><path d="M26 0h18l20 30-20 30H26l20-30z"/></svg>
    <div class="step" style="left:755px">
      <div class="step-circle" style="background:var(--blue-circle)">
        <svg width="100" height="80" viewBox="0 0 100 80" fill="none" stroke="#fff" stroke-width="5"><circle cx="45" cy="22" r="12" stroke-dasharray="6 3"/><circle cx="45" cy="22" r="5"/><circle cx="18" cy="50" r="8" stroke-dasharray="5 3"/><path d="M58 40h30v28H46V54"/><line x1="40" y1="72" x2="94" y2="72"/></svg>
      </div>
      <div class="step-label">Team Projects</div>
    </div>
  </div>

  <div class="region-rule"></div>
  <div class="region">Washington DC Metro Region and Beyond</div>

  <div class="contact">
    <svg width="22" height="34" viewBox="0 0 22 34" fill="none" stroke="var(--phone-blue)" stroke-width="3"><rect x="2" y="2" width="18" height="30" rx="3"/><line x1="8" y1="27" x2="14" y2="27"/></svg>
    <span>202-555-0147 |&nbsp; 410-555-0186</span>
    <svg class="web" width="28" height="28" viewBox="0 0 28 28" fill="none" stroke="var(--phone-blue)" stroke-width="2"><circle cx="14" cy="14" r="12"/><ellipse cx="14" cy="14" rx="5" ry="12"/><line x1="2" y1="14" x2="26" y2="14"/></svg>
    <span>www.PathVerdanta.example</span>
  </div>
</main>
</body>
</html>
```